Letterhead and Envelope Design for Investment Company

We need a letterhead and envelope design.
We are a family owned investment company doing direct investments into other family owned businesses.
I have attached all our current marketing material including our logo for reference.

Our under construction website can be found here:
https://owen-darby-qk7m.sitebrella.example/
password: Marrowdale

Target Market(s)

Bankers, business owners, financial partners

Industry/Entity Type

Investment

Colors

Designer to choose colors to be used in the design.

Requirements
Must have
• Logo, and company information

```html
<!DOCTYPE html>
<html lang="en">
<head>
<meta charset="utf-8">
<title>Marrowdale Holdings Inc. – Letterhead</title>
<link rel="stylesheet" href="https://fonts.googleapis.com/css2?family=PT+Sans:wght@400;700&display=swap">
<style>
  :root {
    --backdrop: #e6d9a2;
    --paper: #ffffff;
    --gold: #d9a521;
    --gold-soft: #f3ead3;
    --grey-band: #b9b9b9;
    --grey-soft: #efefef;
    --grey-faint: #f5f5f3;
    --ink: #4a4a4a;
  }
  * { margin: 0; padding: 0; box-sizing: border-box; }
  html, body {
    width: 1200px; height: 784px; overflow: hidden;
    background: var(--backdrop);
    font-family: "PT Sans", Arial, sans-serif;
  }
  .letterhead {
    position: absolute; left: 345px; top: 32px;
    width: 510px; height: 720px;
    background: var(--paper);
    box-shadow: 0 6px 18px rgba(120, 100, 40, 0.25);
    overflow: hidden;
  }
  .letterhead__art { position: absolute; inset: 0; }
  .brand {
    position: absolute; left: 72px; top: 28px;
    display: flex; align-items: center; gap: 9px;
  }
  .brand__mark {
    width: 14px; height: 14px; background: var(--gold);
  }
  .brand__name {
    font-size: 19px; font-weight: 700; letter-spacing: 2px;
    color: var(--ink); text-transform: uppercase; white-space: nowrap;
  }
  .contact {
    position: absolute; left: 14px; top: 668px;
    display: flex; flex-direction: column; gap: 4px;
    font-size: 9.5px; color: var(--ink); white-space: nowrap;
  }
  .contact__row { display: flex; align-items: center; gap: 16px; }
  .contact__item { display: flex; align-items: center; gap: 5px; }
  .contact__icon { width: 9px; height: 9px; flex: none; }
  .website {
    position: absolute; right: 16px; bottom: 7px;
    font-size: 11px; font-weight: 700; color: #fff; white-space: nowrap;
  }
</style>
</head>
<body>
  <main class="letterhead">
    <svg class="letterhead__art" width="510" height="720" viewBox="0 0 510 720" aria-hidden="true">
      <defs>
        <linearGradient id="band-grey" x1="0" y1="0" x2="0" y2="1">
          <stop offset="0" stop-color="#dcdcdc"/>
          <stop offset="0.5" stop-color="#b9b9b9"/>
          <stop offset="1" stop-color="#ffffff"/>
        </linearGradient>
      </defs>
      <rect class="header-bar-gold" x="0" y="18" width="60" height="6" fill="var(--gold)"/>
      <rect class="header-bar-grey" x="220" y="62" width="290" height="10" fill="url(#band-grey)"/>
      <rect x="405" y="82" width="40" height="30" rx="3" fill="var(--gold-soft)"/>
      <rect x="390" y="116" width="50" height="38" rx="3" fill="var(--grey-soft)"/>
      <rect x="448" y="104" width="56" height="44" rx="3" fill="var(--grey-soft)"/>
      <rect x="415" y="164" width="80" height="56" rx="4" fill="var(--gold-soft)"/>
      <rect x="475" y="82" width="30" height="18" rx="3" fill="var(--grey-faint)"/>
      <path d="M0,470 C40,560 150,600 300,640 C360,656 420,690 460,720 L0,720 Z" fill="var(--grey-faint)"/>
      <path d="M0,420 C30,520 120,560 250,600 C300,615 330,628 350,640 C300,615 150,585 60,540 C30,520 8,480 0,450 Z" fill="var(--gold-soft)"/>
      <path d="M0,520 C80,600 260,610 400,700 C300,650 120,640 0,560 Z" fill="var(--grey-soft)"/>
      <rect x="0" y="660" width="380" height="2" fill="#cfcfcf"/>
      <rect x="0" y="713" width="340" height="4" fill="var(--gold)"/>
      <polygon points="318,694 510,694 510,720 340,720" fill="var(--gold)"/>
    </svg>

    <div class="brand">
      <span class="brand__mark"></span>
      <span class="brand__name">Marrowdale Holdings Inc.</span>
    </div>

    <div class="contact">
      <div class="contact__row">
        <span class="contact__item">
          <svg class="contact__icon" viewBox="0 0 10 10"><circle cx="5" cy="5" r="4.5" fill="var(--gold)"/><circle cx="5" cy="5" r="1.6" fill="#fff"/></svg>
          Marrowdale Holdings, Inc., 48 Orchard Ave. NE, Suite 210, Linwood Falls, IA 50999
        </span>
      </div>
      <div class="contact__row">
        <span class="contact__item">
          <svg class="contact__icon" viewBox="0 0 10 10"><rect width="10" height="10" rx="2" fill="var(--gold)"/></svg>
          555-014-2288
        </span>
        <span class="contact__item">inquiries@marrowdaleholdings.example</span>
      </div>
    </div>

    <div class="website">www.marrowdaleholdings.example</div>
  </main>
</body>
</html>
```